Operating Model for KMR

Please convert the diagram on slide 3 to a professional design. Slides 1 and 2 gives a sense of the colour scheme - although not as bold as those - but sympathetic colours. But the KMR logo is to appear on the slide.
Further instructions in the slide

```html
<!DOCTYPE html>
<html lang="en">
<head>
<meta charset="utf-8">
<title>KMR Operating Model</title>
<link href="https://fonts.googleapis.com/css2?family=Roboto+Condensed:wght@500;700&display=swap" rel="stylesheet">
<style>
  :root {
    --sand: #E6AF70;
    --sand-side-low: #7B6438;
    --sand-side: #5A4128;
    --slate: #A8B3B2;
    --slate-side: #4E5458;
    --olive: #AFB21E;
    --olive-side: #4B5A05;
    --ochre: #C68B35;
    --ochre-side: #3C2A12;
    --crimson: #A91E42;
    --red: #C8102E;
    --coral: #EC724B;
    --ring-grey: #E2E2E2;
    --ring-text: #5A5A5A;
    --head-sand: #F0B477;
    --head-slate: #BEC7C7;
    --head-olive: #B5B51D;
    --white: #FFFFFF;
  }
  html, body { margin: 0; padding: 0; overflow: hidden; background: var(--white); }
  .canvas { width: 1200px; height: 1080px; overflow: hidden; background: var(--white); }
  .model { display: block; width: 1200px; height: 1080px; font-family: "Roboto Condensed", sans-serif; }
  .seg-label { fill: var(--white); font-weight: 700; font-size: 20px; text-anchor: middle; }
  .seg-label--lg { font-size: 23px; }
  .ring-label { fill: var(--white); font-weight: 700; font-size: 24px; letter-spacing: 1.5px; }
  .band-label { fill: var(--ring-text); font-weight: 500; font-size: 14px; letter-spacing: .5px; }
  .core-label { fill: var(--white); font-weight: 700; font-size: 27px; letter-spacing: 1px; }
  .brand { fill: var(--white); font-weight: 700; font-size: 44px; text-anchor: middle; letter-spacing: 2px; }
  .heading { font-weight: 700; font-size: 36px; letter-spacing: 1px; }
  .heading--planning { fill: var(--head-sand); }
  .heading--attracting { fill: var(--head-slate); }
  .heading--building { fill: var(--head-olive); }
  .divider { fill: var(--white); }
</style>
</head>
<body>
<div class="canvas">
<svg class="model" viewBox="0 0 1287 1158" preserveAspectRatio="none" role="img" aria-label="KMR operating model diagram">
  <defs>
    <path id="arc-industry" d="M389.6,672.3 A254,254 0 0 1 473,501.2"/>
    <path id="arc-community" d="M473,501.2 A254,254 0 0 1 643,436"/>
    <path id="arc-government" d="M643,436 A254,254 0 0 1 809.6,498.3"/>
    <path id="arc-future" d="M809.6,498.3 A254,254 0 0 1 896,667.9"/>
    <path id="arc-students" d="M448.4,853.3 A254,254 0 0 1 389.6,672.3"/>
    <path id="arc-productivity" d="M857.3,857.5 A272,272 0 0 0 914,666.3"/>
    <path id="arc-quality" d="M643,962 A272,272 0 0 0 857.3,857.5"/>
    <path id="arc-feedback" d="M434.6,864.8 A272,272 0 0 0 643,962"/>
    <path id="arc-schooling" d="M442.1,743.8 A208,208 0 0 1 447.5,618.9"/>
    <path id="arc-community-ed" d="M454.5,602.1 A208,208 0 0 1 599.8,486.5"/>
    <path id="arc-vocational" d="M614.1,484 A208,208 0 0 1 806.9,561.9"/>
    <path id="arc-higher" d="M831.5,602.1 A208,208 0 0 1 823.1,794"/>
    <path id="arc-planning-core" d="M532.1,730.4 A118,118 0 0 1 683.4,579.1"/>
    <path id="arc-renewal-core" d="M745.2,631 A118,118 0 0 1 622.5,806.2"/>
    <path id="arc-head-planning" d="M88.5,612.1 A560,560 0 0 1 298.2,248.7"/>
    <path id="arc-head-attracting" d="M397.5,186.7 A560,560 0 0 1 778.5,146.6"/>
    <path id="arc-head-building" d="M905.9,195.6 A560,560 0 0 1 1190.8,573.6"/>
  </defs>

  <!-- Theme headings -->
  <text class="heading heading--planning"><textPath href="#arc-head-planning" startOffset="50%" text-anchor="middle">PLANNING FOR SKILLING</textPath></text>
  <text class="heading heading--attracting"><textPath href="#arc-head-attracting" startOffset="50%" text-anchor="middle">ATTRACTING STUDENTS</textPath></text>
  <text class="heading heading--building"><textPath href="#arc-head-building" startOffset="50%" text-anchor="middle">BUILDING FUTURE SKILLS</textPath></text>

  <!-- Fan segments -->
  <g class="fan">
    <g class="segment segment--engagement">
      <path transform="translate(-4,36)" fill="var(--sand-side-low)" d="M128,690 A515,515 0 0 1 180.1,464.2 L409.3,576 A260,260 0 0 0 383,690 Z"/>
      <path fill="var(--sand)" d="M128,690 A515,515 0 0 1 180.1,464.2 L409.3,576 A260,260 0 0 0 383,690 Z"/>
    </g>
    <g class="segment segment--data">
      <path transform="translate(-8,26)" fill="var(--sand-side)" d="M166.2,436.5 A540,540 0 0 1 325.6,253.1 L490.2,479.7 A260,260 0 0 0 413.4,567.9 Z"/>
      <path fill="var(--sand)" d="M166.2,436.5 A540,540 0 0 1 325.6,253.1 L490.2,479.7 A260,260 0 0 0 413.4,567.9 Z"/>
    </g>
    <g class="segment segment--innovation">
      <path transform="translate(-10,26)" fill="var(--ochre-side)" d="M1110.8,451.6 A525,525 0 0 1 1167.9,680.8 L903,685.5 A260,260 0 0 0 874.7,572 Z"/>
      <path fill="var(--ochre)" d="M1110.8,451.6 A525,525 0 0 1 1167.9,680.8 L903,685.5 A260,260 0 0 0 874.7,572 Z"/>
    </g>
    <g class="segment segment--quality">
      <path transform="translate(-10,26)" fill="var(--olive-side)" d="M997.6,309.7 A520,520 0 0 1 1097.8,437.9 L870.4,564 A260,260 0 0 0 820.3,499.8 Z"/>
      <path fill="var(--olive)" d="M997.6,309.7 A520,520 0 0 1 1097.8,437.9 L870.4,564 A260,260 0 0 0 820.3,499.8 Z"/>
    </g>
    <g class="segment segment--feedback">
      <path transform="translate(-10,26)" fill="var(--olive-side)" d="M844.2,215.9 A515,515 0 0 1 980.9,301.3 L813.6,493.8 A260,260 0 0 0 744.6,450.7 Z"/>
      <path fill="var(--olive)" d="M844.2,215.9 A515,515 0 0 1 980.9,301.3 L813.6,493.8 A260,260 0 0 0 744.6,450.7 Z"/>
    </g>
    <g class="segment segment--provision">
      <path transform="translate(-10,26)" fill="var(--slate-side)" d="M338.2,238.2 A545,545 0 0 1 576.6,149.1 L611.3,431.9 A260,260 0 0 0 497.6,474.5 Z"/>
      <path fill="var(--slate)" d="M338.2,238.2 A545,545 0 0 1 576.6,149.1 L611.3,431.9 A260,260 0 0 0 497.6,474.5 Z"/>
    </g>
    <g class="segment segment--acquisition">
      <path transform="translate(-10,26)" fill="var(--slate-side)" d="M596.3,157 A535,535 0 0 1 834.7,190.5 L736.2,447.3 A260,260 0 0 0 620.3,431 Z"/>
      <path fill="var(--slate)" d="M596.3,157 A535,535 0 0 1 834.7,190.5 L736.2,447.3 A260,260 0 0 0 620.3,431 Z"/>
    </g>
  </g>

  <!-- Segment labels -->
  <text class="seg-label" transform="translate(255,590)"><tspan x="0" dy="-15">ENGAGEMENT AND</tspan><tspan x="0" dy="22">COLLABORATION</tspan><tspan x="0" dy="22">FRONT DOOR</tspan></text>
  <text class="seg-label" transform="translate(336,405) rotate(35)"><tspan x="0" dy="-4">SKILLS DATA</tspan><tspan x="0" dy="22">AND INSIGHTS</tspan></text>
  <text class="seg-label" transform="translate(500,268) rotate(90)"><tspan x="0" dy="-26">PROVISION</tspan><tspan x="0" dy="22">PLANNING</tspan><tspan x="0" dy="22">REGIONAL</tspan><tspan x="0" dy="22">SKILLS PLAN</tspan></text>
  <text class="seg-label" transform="translate(695,275) rotate(-90)"><tspan x="0" dy="-15">STUDENT</tspan><tspan x="0" dy="22">ACQUISITION</tspan><tspan x="0" dy="22">AND GUIDANCE</tspan></text>
  <text class="seg-label" transform="translate(848,330) rotate(-55)"><tspan x="0" dy="-15">SKILLS FEEDBACK</tspan><tspan x="0" dy="22">EMPLOYERS AND</tspan><tspan x="0" dy="22">STUDENTS</tspan></text>
  <text class="seg-label" transform="translate(968,432) rotate(-35)"><tspan x="0" dy="-26">QUALITY</tspan><tspan x="0" dy="22">WORKFORCE</tspan><tspan x="0" dy="22">COURSE DESIGN</tspan><tspan x="0" dy="22">RECOGNITION</tspan></text>
  <text class="seg-label seg-label--lg" transform="translate(1030,580)"><tspan x="0" dy="-4">SKILLS</tspan><tspan x="0" dy="26">INNOVATION</tspan></text>

  <!-- Stakeholder ring -->
  <g class="ring">
    <path fill="var(--crimson)" d="M420.8,876.4 A290,290 0 0 1 833.3,471.1 L797.8,511.9 A236,236 0 0 0 462.2,841.7 Z"/>
    <path fill="var(--coral)" d="M833.3,471.1 A290,290 0 1 1 420.8,876.4 L462.2,841.7 A236,236 0 1 0 797.8,511.9 Z"/>
    <g class="divider">
      <polygon points="881,680 929,680 905,698" transform="rotate(270 643 690)"/>
      <polygon points="881,680 929,680 905,698" transform="rotate(311 643 690)"/>
      <polygon points="881,680 929,680 905,698" transform="rotate(355 643 690)"/>
      <polygon points="881,680 929,680 905,698" transform="rotate(38 643 690)"/>
      <polygon points="881,680 929,680 905,698" transform="rotate(90 643 690)"/>
      <polygon points="881,680 929,680 905,698" transform="rotate(140 643 690)"/>
      <polygon points="881,680 929,680 905,698" transform="rotate(184 643 690)"/>
      <polygon points="881,680 929,680 905,698" transform="rotate(228 643 690)"/>
    </g>
    <text class="ring-label"><textPath href="#arc-industry" startOffset="50%" text-anchor="middle">INDUSTRY</textPath></text>
    <text class="ring-label"><textPath href="#arc-community" startOffset="50%" text-anchor="middle">COMMUNITY</textPath></text>
    <text class="ring-label"><textPath href="#arc-government" startOffset="50%" text-anchor="middle">GOVERNMENT</textPath></text>
    <text class="ring-label"><textPath href="#arc-future" startOffset="50%" text-anchor="middle">FUTURE SKILLS</textPath></text>
    <text class="ring-label"><textPath href="#arc-students" startOffset="50%" text-anchor="middle">STUDENTS</textPath></text>
    <text class="ring-label"><textPath href="#arc-productivity" startOffset="50%" text-anchor="middle">PRODUCTIVITY</textPath></text>
    <text class="ring-label"><textPath href="#arc-quality" startOffset="50%" text-anchor="middle">QUALITY</textPath></text>
    <text class="ring-label"><textPath href="#arc-feedback" startOffset="50%" text-anchor="middle">FEEDBACK</textPath></text>
  </g>

  <!-- Education band -->
  <circle class="band" cx="643" cy="690" r="236" fill="var(--ring-grey)"/>
  <text class="band-label"><textPath href="#arc-schooling" startOffset="50%" text-anchor="middle">SCHOOLING</textPath></text>
  <text class="band-label"><textPath href="#arc-community-ed" startOffset="50%" text-anchor="middle">COMMUNITY EDUCATION</textPath></text>
  <text class="band-label"><textPath href="#arc-vocational" startOffset="50%" text-anchor="middle">VOCATIONAL  EDUCATION</textPath></text>
  <text class="band-label"><textPath href="#arc-higher" startOffset="50%" text-anchor="middle">HIGHER EDUCATION</textPath></text>

  <!-- Core -->
  <path class="core core--planning" fill="var(--red)" d="M536.1,813 A163,163 0 0 1 749.9,567 Z"/>
  <path class="core core--renewal" fill="var(--coral)" d="M749.9,567 A163,163 0 0 1 536.1,813 Z"/>
  <text class="core-label"><textPath href="#arc-planning-core" startOffset="50%" text-anchor="middle">SKILLS PLANNING</textPath></text>
  <text class="core-label"><textPath href="#arc-renewal-core" startOffset="50%" text-anchor="middle">SKILLS RENEWAL</textPath></text>
  <text class="brand" x="643" y="706">KMR</text>
</svg>
</div>
</body>
</html>
```